Mobile Fitness snd Therapy Business Card Design

I need a business card designed for my mobile fitness and therapy business.

Please view the images that I have uploaded. I like the simplicity of the design that I have attached. I adapted it with my information

Target Market(s)

Those seeking personal training, injury rehabilitation or massage therapy.

Industry/Entity Type

Business

Contact Information for Business Card

Derek Holloway - MSc, CAT(C), RMT, CSCS, Pn2
e-mail: derek@bravuumfit.example
website: www.bravuumfit.example
instagram: @derek_holloway

Font styles to use
Sans Serif

Colors
3176b5
0355a3

Requirements
Must have
• "Contact us to receive a FREE assessment"
• Services offered:
• Personal Training
• Golf Fitness
• Injury Rehab
• Massage Therapy
• Yoga
Nice to have
• Consistent colours with brand
• - Dark Blue: #232837
• - Blue: #5096f0
• Consistent look/feel with the website: www.bravuumfit.example

```html
<!DOCTYPE html>
<html lang="en">
<head>
<meta charset="utf-8">
<title>Bravuum Business Card</title>
<link rel="stylesheet" href="https://fonts.googleapis.com/css2?family=Roboto:wght@400;500;700&family=Roboto+Condensed:wght@700&display=swap">
<style>
  :root {
    --page: #e6e6e6;
    --card-light: #f7f7f7;
    --card-dark: #232837;
    --ink: #232837;
    --blue: #2b5cd8;
    --text-grey: #4a4a4a;
    --divider-blue: #3d6fe0;
    --white: #ffffff;
  }
  * { margin: 0; padding: 0; box-sizing: border-box; }
  html, body {
    width: 1200px; height: 960px; overflow: hidden;
    background: var(--page);
    font-family: "Roboto", Arial, sans-serif;
  }
  .card {
    position: absolute;
    width: 601px; height: 343px;
  }
  .card--front { left: 314px; top: 113px; background: var(--card-light); }
  .card--back { left: 311px; top: 472px; background: var(--card-dark); }

  .brand { position: absolute; }
  .brand__name {
    font-weight: 700;
    letter-spacing: 3px;
    line-height: 1;
  }
  .brand__tagline {
    font-weight: 700;
    line-height: 1;
    white-space: nowrap;
  }
  .card--front .brand { left: 52px; top: 50px; }
  .card--front .brand__name { font-size: 38px; color: var(--ink); }
  .card--front .brand__tagline { font-size: 12.5px; letter-spacing: 1.6px; color: var(--ink); margin-top: 8px; }

  .card--back .brand { left: 0; right: 0; top: 138px; text-align: center; }
  .card--back .brand__name { font-size: 54px; color: var(--white); letter-spacing: 5px; }
  .card--back .brand__tagline { font-size: 18.5px; letter-spacing: 2.6px; color: var(--white); margin-top: 12px; }

  .person { position: absolute; left: 52px; top: 125px; }
  .person__name {
    font-family: "Roboto Condensed", "Arial Narrow", sans-serif;
    font-size: 23px; color: var(--blue); line-height: 1;
  }
  .person__credentials {
    font-family: "Roboto Condensed", "Arial Narrow", sans-serif;
    font-size: 10.5px; color: var(--blue); margin-top: 4px;
  }

  .contacts { position: absolute; left: 53px; top: 172px; list-style: none; }
  .contacts__item {
    display: flex; align-items: center; gap: 7px;
    font-size: 14.5px; color: var(--text-grey); height: 19px;
  }
  .contacts__icon { width: 14px; height: 14px; flex: none; }

  .cta {
    position: absolute; left: 49px; top: 249px;
    width: 450px; height: 31px; border-radius: 16px;
    background: var(--blue); color: var(--white);
    font-size: 18px; font-weight: 700;
    display: flex; align-items: center; justify-content: center;
    white-space: nowrap;
  }
  .services {
    position: absolute; left: 49px; top: 286px;
    font-size: 13.6px; color: var(--text-grey); white-space: nowrap;
  }
  .services__divider { color: var(--divider-blue); padding: 0 2px; }
</style>
</head>
<body>

<section class="card card--front">
  <div class="brand">
    <div class="brand__name">BRAVUUM</div>
    <div class="brand__tagline">NUTRITION - FITNESS - HEALTH</div>
  </div>

  <div class="person">
    <div class="person__name">DEREK HOLLOWAY</div>
    <div class="person__credentials">MSC, CAT(C), RMT, CSCS, PN2</div>
  </div>

  <ul class="contacts">
    <li class="contacts__item">
      <svg class="contacts__icon" viewBox="0 0 14 14" aria-hidden="true">
        <rect x="1" y="3" width="12" height="8.5" rx="1" fill="#2b5cd8"/>
        <path d="M1.5 3.8 L7 7.8 L12.5 3.8" fill="none" stroke="#f7f7f7" stroke-width="1.2"/>
      </svg>
      derek@bravuumfit.example
    </li>
    <li class="contacts__item">
      <svg class="contacts__icon" viewBox="0 0 14 14" aria-hidden="true">
        <circle cx="7" cy="7" r="6" fill="#2b5cd8"/>
        <path d="M1.5 7 H12.5 M7 1 C4.5 4 4.5 10 7 13 M7 1 C9.5 4 9.5 10 7 13" fill="none" stroke="#f7f7f7" stroke-width="1"/>
      </svg>
      www.bravuumfit.example
    </li>
    <li class="contacts__item">
      <svg class="contacts__icon" viewBox="0 0 14 14" aria-hidden="true">
        <circle cx="7" cy="7" r="6" fill="#2b5cd8"/>
      </svg>
      @derek_holloway
    </li>
  </ul>

  <div class="cta">CONTACT US TO RECEIVE A FREE ASSESSMENT</div>

  <p class="services">
    Personal Training <span class="services__divider">|</span> Golf Fitness <span class="services__divider">|</span> Injury Rehab <span class="services__divider">|</span> Massage Therapy <span class="services__divider">|</span> Yoga
  </p>
</section>

<section class="card card--back">
  <div class="brand">
    <div class="brand__name">BRAVUUM</div>
    <div class="brand__tagline">NUTRITION - FITNESS - HEALTH</div>
  </div>
</section>

</body>
</html>
```